Migration Lawyers

Company: Dunstan & Co Lawyers & Migration Agents

Name: Graham Dunstan BEc, LLB
Address: Level 18, 72 Hollis Street
Sydney, NSW, Australia 2000

Ph: +61 2 9384 5207
M: 0428316540
E: graham@permitpath-example.org.au
W: www.permitpath-example.org.au

Target Market(s)

Migration Clients

Industry/Entity Type

It Company

Font styles to use
Script

Requirements
Must have
• Logo
Should not have
• Please scale the format to the printing size attached

```html
<!DOCTYPE html>
<html lang="en">
<head>
<meta charset="utf-8">
<title>Dunstan &amp; Co — Business Card</title>
<link rel="stylesheet" href="https://fonts.googleapis.com/css2?family=Pinyon+Script&family=Tinos:ital,wght@0,700;1,400;1,700&display=swap">
<style>
  :root {
    --ink: #0b0b0b;
    --paper: #ffffff;
    --sheet: #ffffff;
    --frame: #b9b9c2;
    --muted: #7a7a7a;
    --band-peak: #7c7c7c;
    --band-mid: #3e3e3e;
    --ring: #1a1a1a;
  }
  * { margin: 0; padding: 0; box-sizing: border-box; }
  html, body { width: 900px; height: 1200px; overflow: hidden; background: var(--sheet); }
  .sheet {
    position: relative; width: 900px; height: 1200px;
    border: 1px solid var(--frame);
    font-family: "Tinos", "Times New Roman", serif;
  }
  .side-label {
    position: absolute; left: 45px;
    font-family: "Tinos", "Times New Roman", serif;
    font-style: italic; font-weight: 400; font-size: 32px; color: var(--ink);
  }
  .side-label--front { top: 14px; }
  .side-label--back { top: 612px; }

  /* Front */
  .card-front {
    position: absolute; left: 48px; top: 67px; width: 806px; height: 521px;
    border: 1px solid var(--frame); background: var(--paper); overflow: hidden;
  }
  .card-front__panel {
    position: absolute; left: 385px; top: 0; right: 0; bottom: 0; background: var(--ink);
  }
  .brand { position: absolute; display: flex; align-items: center; color: var(--ink); font-weight: 700; font-style: normal; }
  .brand__dot { flex: none; border-radius: 50%; background: var(--ink); }
  .brand__name { display: block; line-height: 1; }
  .brand__tagline { display: block; line-height: 1.2; }
  .brand--front { left: 22px; top: 200px; gap: 12px; }
  .brand--front .brand__dot { width: 88px; height: 88px; }
  .brand--front .brand__name { font-size: 30px; }
  .brand--front .brand__tagline { font-size: 13px; margin-top: 3px; }

  .website {
    position: absolute; left: 0; width: 385px; top: 466px; text-align: center;
    font-style: italic; font-weight: 700; font-size: 18px; color: var(--muted);
  }
  .holder {
    position: absolute; right: 38px; top: 52px;
    font-family: "Pinyon Script", cursive; font-size: 33px; color: var(--paper);
  }
  .contact-list { position: absolute; right: 36px; top: 137px; list-style: none; }
  .contact-list li {
    display: flex; justify-content: flex-end; align-items: center; gap: 10px;
    height: 50px; color: var(--paper); font-style: italic; font-weight: 700; font-size: 24px;
  }
  .contact-list li.contact--email { font-size: 18px; }
  .contact__icon { width: 36px; height: 36px; flex: none; }
  .office {
    position: absolute; right: 38px; top: 378px; text-align: right;
    color: var(--paper); font-style: italic; font-weight: 700; line-height: 1.25;
  }
  .office__firm { font-size: 22px; }
  .office__tagline { font-size: 14px; margin-bottom: 6px; }
  .office__address { font-size: 22px; }

  /* Back */
  .card-back {
    position: absolute; left: 48px; top: 663px; width: 808px; height: 523px;
    background: var(--ink); overflow: hidden;
  }
  .card-back__band {
    position: absolute; left: 0; right: 0; top: 177px; height: 146px;
    background: linear-gradient(to bottom, var(--ink) 0%, var(--band-mid) 22%, var(--band-peak) 45%, var(--band-peak) 58%, var(--band-mid) 80%, var(--ink) 100%);
  }
  .brand--back { left: 80px; top: 85px; gap: 30px; color: var(--paper); }
  .brand--back .brand__dot {
    width: 370px; height: 370px; background: var(--paper);
    box-shadow: inset 0 0 0 14px var(--paper), inset 0 0 0 16px var(--ring);
  }
  .brand--back .brand__name { font-size: 40px; }
  .brand--back .brand__tagline { font-size: 16px; margin-top: 6px; }
</style>
</head>
<body>
<main class="sheet">
  <p class="side-label side-label--front">card_front</p>
  <section class="card-front" aria-label="Card front">
    <div class="brand brand--front">
      <span class="brand__dot"></span>
      <span><span class="brand__name">Dunstan &amp; Co</span><span class="brand__tagline">Lawyers &amp; Migration Agents</span></span>
    </div>
    <p class="website">www.permitpath-example.org.au</p>

    <div class="card-front__panel">
      <p class="holder">Graham Dunstan BEc, LLB</p>
      <ul class="contact-list">
        <li class="contact--phone">+61 2 9384 5207
          <svg class="contact__icon" viewBox="0 0 36 36" aria-hidden="true"><circle cx="18" cy="18" r="17" fill="#fff"/><path d="M12 9c1.5-1 2.5 0 3.5 2s.5 2.5-.8 3.3c.8 2.5 2.5 4.5 5 5.8 1-1.2 1.8-1.5 3.5-.5s2.5 2 1.3 3.4c-1.5 1.8-3.5 2-6 .7-4-2-7-5.7-8-9.6-.5-2.3.2-4 1.5-5.1z" fill="#555"/></svg>
        </li>
        <li class="contact--mobile">0428316540
          <svg class="contact__icon" viewBox="0 0 36 36" aria-hidden="true"><circle cx="18" cy="18" r="17" fill="#fff"/><rect x="13" y="7" width="10" height="22" rx="2" fill="none" stroke="#555" stroke-width="1.6"/><rect x="15" y="10" width="6" height="6" fill="#777"/><g fill="#777"><circle cx="15.5" cy="20" r=".9"/><circle cx="18" cy="20" r=".9"/><circle cx="20.5" cy="20" r=".9"/><circle cx="15.5" cy="23" r=".9"/><circle cx="18" cy="23" r=".9"/><circle cx="20.5" cy="23" r=".9"/></g></svg>
        </li>
        <li class="contact--email">graham@permitpath-example.org.au
          <svg class="contact__icon" viewBox="0 0 36 36" aria-hidden="true"><circle cx="18" cy="18" r="17" fill="#fff"/><rect x="9" y="12" width="18" height="12" fill="#666"/><path d="M9 12l9 7 9-7" fill="none" stroke="#ddd" stroke-width="1.3"/></svg>
        </li>
      </ul>
      <div class="office">
        <p class="office__firm">Dunstan &amp; Co</p>
        <p class="office__tagline">Lawyers &amp; Migration Agents</p>
        <p class="office__address">Level 18, 72 Hollis Street<br>Australia, Sydney, NSW, 2000</p>
      </div>
    </div>
  </section>

  <p class="side-label side-label--back">card_back</p>
  <section class="card-back" aria-label="Card back">
    <div class="card-back__band"></div>
    <div class="brand brand--back">
      <span class="brand__dot"></span>
      <span><span class="brand__name">Dunstan &amp; Co</span><span class="brand__tagline">Lawyers &amp; Migration Agents</span></span>
    </div>
  </section>
</main>
</body>
</html>
```